Essential Oil 15ml - package of 6

Design of a box of 6 different essential oils.
+ design of the bottle stickers
My bottles are 15ml clear blue glass.

The pictures attached are my competitors...

Target Market(s)

BRAMBLEWICK USA

Font styles to use
Serif

Requirements
Must have
• Our Bramblewick + "essential oil" and type (lavender, eucalyptus etc....)
• 15ml - 0.50 fl.oz.
• special color for the oil type.

```html
<!DOCTYPE html>
<html lang="en">
<head>
<meta charset="utf-8">
<title>Bramblewick Essential Oil Labels</title>
<link rel="stylesheet" href="https://fonts.googleapis.com/css2?family=Playfair+Display:ital,wght@0,400;1,400&family=Josefin+Sans:wght@400;600&display=swap">
<style>
  :root {
    --page: #f6f6f6;
    --band: #0b0b0c;
    --white: #ffffff;
    --soft-white: rgba(255,255,255,0.88);
    --gold: #d99a3a;
    --rule: rgba(255,255,255,0.75);
    --eucalyptus-a: #2fbab6; --eucalyptus-b: #b4eaee;
    --lavender-a: #7d479f;   --lavender-b: #cf94d6;
    --rosemary-a: #d22f6a;   --rosemary-b: #f08db2;
    --teatree-a: #3fae3a;    --teatree-b: #cfe22c;
    --grapefruit-a: #cc1a1f; --grapefruit-b: #ec3a3a;
    --orange-a: #ec7f18;     --orange-b: #f8d62c;
  }
  * { box-sizing: border-box; }
  html, body {
    margin: 0; width: 1200px; height: 902px; overflow: hidden;
    background: var(--page);
  }
  .label-set {
    position: absolute; left: 85px; top: 417px;
    display: flex; gap: 16px;
  }
  .label {
    width: 157px;
    display: flex; flex-direction: column;
    color: var(--white);
  }
  .label__face {
    height: 111px;
    background: linear-gradient(120deg, var(--c-a) 0%, var(--c-b) 55%, var(--c-a) 100%);
    display: flex; flex-direction: column; align-items: center;
    padding-top: 13px;
  }
  .label__brand {
    font-family: "Playfair Display", serif;
    font-weight: 400; font-size: 21px; line-height: 1;
    white-space: nowrap;
  }
  .label__divider {
    display: flex; align-items: center; gap: 6px;
    margin-top: 12px; width: 116px;
  }
  .label__divider::before, .label__divider::after {
    content: ""; flex: 1; height: 1px; background: var(--rule);
  }
  .label__dot { width: 5px; height: 5px; border-radius: 50%; background: var(--white); }
  .label__kind {
    margin-top: 7px;
    font-family: "Josefin Sans", sans-serif; font-weight: 600;
    font-size: 13px; letter-spacing: 1.2px; line-height: 1;
    white-space: nowrap;
  }
  .label__oil {
    margin-top: 4px;
    font-family: "Playfair Display", serif; font-style: italic;
    font-size: 12px; letter-spacing: 2px; line-height: 1;
    color: var(--soft-white); white-space: nowrap;
  }
  .label__info {
    height: 56px;
    background: var(--band);
    border-top: 2px solid var(--gold);
    display: flex; flex-direction: column; align-items: center;
    padding-top: 7px;
  }
  .label__botanical {
    font-family: "Playfair Display", serif; font-style: italic;
    font-size: 7.5px; letter-spacing: 0.8px; line-height: 1;
    padding-bottom: 4px; width: 136px; text-align: center;
    border-bottom: 1px solid var(--rule);
    color: var(--white); white-space: nowrap;
  }
  .label__specs {
    display: flex; align-items: stretch; margin-top: 3px;
    font-family: "Josefin Sans", sans-serif; font-weight: 400;
    color: var(--white);
  }
  .label__volume {
    width: 60px; text-align: center; font-size: 12.5px; letter-spacing: 1px;
    padding-top: 7px;
  }
  .label__purity {
    width: 60px; text-align: center; border-left: 1px solid var(--rule);
    font-size: 12px; line-height: 1; padding-top: 3px; letter-spacing: 1px;
  }
  .label__purity small {
    display: block; font-size: 6px; letter-spacing: 0.6px; margin-top: 1px;
    color: var(--white);
  }
  .label__stripe {
    height: 12px;
    border-top: 2px solid var(--gold);
    background: linear-gradient(90deg, var(--c-a), var(--c-b), var(--c-a));
  }
  .label--eucalyptus { --c-a: var(--eucalyptus-a); --c-b: var(--eucalyptus-b); }
  .label--lavender   { --c-a: var(--lavender-a);   --c-b: var(--lavender-b); }
  .label--rosemary   { --c-a: var(--rosemary-a);   --c-b: var(--rosemary-b); }
  .label--teatree    { --c-a: var(--teatree-a);    --c-b: var(--teatree-b); }
  .label--grapefruit { --c-a: var(--grapefruit-a); --c-b: var(--grapefruit-b); }
  .label--orange     { --c-a: var(--orange-a);     --c-b: var(--orange-b); }
</style>
</head>
<body>
<main class="label-set">
  <section class="label label--eucalyptus">
    <div class="label__face">
      <div class="label__brand">Bramblewick</div>
      <div class="label__divider"><span class="label__dot"></span></div>
      <div class="label__kind">ESSENTIAL OIL</div>
      <div class="label__oil">eucalyptus</div>
    </div>
    <div class="label__info">
      <div class="label__botanical">• eucalyptus globulus •</div>
      <div class="label__specs">
        <div class="label__volume">15 ml</div>
        <div class="label__purity">100 %<small>pure natural</small></div>
      </div>
    </div>
    <div class="label__stripe"></div>
  </section>
  <section class="label label--lavender">
    <div class="label__face">
      <div class="label__brand">Bramblewick</div>
      <div class="label__divider"><span class="label__dot"></span></div>
      <div class="label__kind">ESSENTIAL OIL</div>
      <div class="label__oil">lavender</div>
    </div>
    <div class="label__info">
      <div class="label__botanical">• lavandula •</div>
      <div class="label__specs">
        <div class="label__volume">15 ml</div>
        <div class="label__purity">100 %<small>pure natural</small></div>
      </div>
    </div>
    <div class="label__stripe"></div>
  </section>
  <section class="label label--rosemary">
    <div class="label__face">
      <div class="label__brand">Bramblewick</div>
      <div class="label__divider"><span class="label__dot"></span></div>
      <div class="label__kind">ESSENTIAL OIL</div>
      <div class="label__oil">rosemary</div>
    </div>
    <div class="label__info">
      <div class="label__botanical">• rosmarinus officinalis •</div>
      <div class="label__specs">
        <div class="label__volume">15 ml</div>
        <div class="label__purity">100 %<small>pure natural</small></div>
      </div>
    </div>
    <div class="label__stripe"></div>
  </section>
  <section class="label label--teatree">
    <div class="label__face">
      <div class="label__brand">Bramblewick</div>
      <div class="label__divider"><span class="label__dot"></span></div>
      <div class="label__kind">ESSENTIAL OIL</div>
      <div class="label__oil">tea tree</div>
    </div>
    <div class="label__info">
      <div class="label__botanical">• melaleuca alternifolia •</div>
      <div class="label__specs">
        <div class="label__volume">15 ml</div>
        <div class="label__purity">100 %<small>pure natural</small></div>
      </div>
    </div>
    <div class="label__stripe"></div>
  </section>
  <section class="label label--grapefruit">
    <div class="label__face">
      <div class="label__brand">Bramblewick</div>
      <div class="label__divider"><span class="label__dot"></span></div>
      <div class="label__kind">ESSENTIAL OIL</div>
      <div class="label__oil">grapefruit</div>
    </div>
    <div class="label__info">
      <div class="label__botanical">• citrus × paradisi •</div>
      <div class="label__specs">
        <div class="label__volume">15 ml</div>
        <div class="label__purity">100 %<small>pure natural</small></div>
      </div>
    </div>
    <div class="label__stripe"></div>
  </section>
  <section class="label label--orange">
    <div class="label__face">
      <div class="label__brand">Bramblewick</div>
      <div class="label__divider"><span class="label__dot"></span></div>
      <div class="label__kind">ESSENTIAL OIL</div>
      <div class="label__oil">sweet orange</div>
    </div>
    <div class="label__info">
      <div class="label__botanical">• citrus aurantium •</div>
      <div class="label__specs">
        <div class="label__volume">15 ml</div>
        <div class="label__purity">100 %<small>pure natural</small></div>
      </div>
    </div>
    <div class="label__stripe"></div>
  </section>
</main>
</body>
</html>
```